Strong, modern, clean Business Card design

Looking for a stunning, but CLEAN business card design. While we are a faith-based organization, we do NOT want this to look religious.

Industry/Entity Type

Non-Profit

Contact Information for Business Card

Dale Munroe | Lead Pastor
dale@BrightHarvestHope.org
970-555-0148
PO Box 7316
Elmhaven, WY 80571

Font styles to use
Serif
Sans Serif

Requirements
Should not have
• Religious imagery or symbolism

```html
<!DOCTYPE html>
<html lang="en">
<head>
<meta charset="utf-8">
<title>Dale Munroe – Lead Pastor</title>
<link rel="stylesheet" href="https://fonts.googleapis.com/css2?family=Arimo:wght@400&family=Tinos:wght@400&display=swap">
<style>
  :root {
    --slate-blue: #4d7a94;
    --teal: #4a8fa3;
    --shadow-black: #111111;
    --paper: #ffffff;
    --ink: #141414;
    --badge-yellow: #f1f053;
  }
  html, body {
    margin: 0;
    padding: 0;
    width: 1200px;
    height: 686px;
    overflow: hidden;
    background: var(--paper);
  }
  .card {
    position: relative;
    width: 1200px;
    height: 686px;
    overflow: hidden;
    background: var(--slate-blue);
  }
  .card-shapes {
    position: absolute;
    inset: 0;
    width: 1200px;
    height: 686px;
  }
  .brand {
    position: absolute;
    left: 40px;
    top: 205px;
    width: 380px;
    text-align: center;
    font-family: "Tinos", "Times New Roman", serif;
    font-weight: 400;
    color: var(--slate-blue);
    text-transform: uppercase;
    letter-spacing: 6px;
    font-size: 40px;
    line-height: 1.25;
  }
  .identity {
    position: absolute;
    left: 600px;
    top: 84px;
    width: 570px;
    text-align: center;
    color: var(--ink);
  }
  .identity-name {
    margin: 0;
    font-family: "Arimo", Arial, sans-serif;
    font-weight: 400;
    font-size: 58px;
    letter-spacing: 2px;
    line-height: 1;
    text-transform: uppercase;
  }
  .identity-role {
    margin: 12px 0 0;
    font-family: "Tinos", "Times New Roman", serif;
    font-weight: 400;
    font-size: 56px;
    line-height: 1;
  }
  .contact-list {
    position: absolute;
    left: 688px;
    top: 0;
    margin: 0;
    padding: 0;
    list-style: none;
    font-family: "Arimo", Arial, sans-serif;
    font-size: 32px;
    color: var(--ink);
  }
  .contact-item {
    position: absolute;
    left: 0;
    display: flex;
    align-items: flex-start;
    white-space: nowrap;
  }
  .contact-item--email { top: 318px; }
  .contact-item--address { top: 403px; }
  .contact-item--phone { top: 534px; }
  .contact-icon {
    width: 76px;
    height: 62px;
    flex: none;
    margin-right: 10px;
  }
  .contact-text {
    margin-top: 12px;
    line-height: 46px;
  }
  .contact-item--email .contact-text {
    margin-top: 8px;
    font-size: 30px;
  }
  .contact-item--phone .contact-text { margin-top: 8px; }
</style>
</head>
<body>
<div class="card">
  <svg class="card-shapes" viewBox="0 0 1050 600" preserveAspectRatio="none" aria-hidden="true">
    <path fill="var(--teal)" d="M355,0 C440,110 500,210 520,258 C570,360 605,470 610,600 L0,600 L0,0 Z"/>
    <path fill="var(--shadow-black)" d="M355,0 C450,130 545,270 545,420 C545,500 520,560 500,600 L0,600 L0,0 Z"/>
    <path fill="var(--paper)" d="M355,0 C450,130 540,260 535,400 C532,490 490,555 450,600 L0,600 L0,0 Z"/>
  </svg>

  <div class="brand">Bright Harvest<br>Hope</div>

  <div class="identity">
    <h1 class="identity-name">Dale Munroe</h1>
    <p class="identity-role">Lead Pastor</p>
  </div>

  <ul class="contact-list">
    <li class="contact-item contact-item--email">
      <svg class="contact-icon" viewBox="0 0 76 62" aria-hidden="true">
        <ellipse cx="38" cy="31" rx="37" ry="30" fill="var(--badge-yellow)"/>
        <rect x="15" y="16" width="46" height="30" fill="var(--shadow-black)"/>
        <path d="M17,18 L38,34 L59,18 M17,44 L32,30 M59,44 L44,30" stroke="var(--badge-yellow)" stroke-width="2" fill="none"/>
      </svg>
      <span class="contact-text">dale@BrightHarvestHope.org</span>
    </li>
    <li class="contact-item contact-item--address">
      <svg class="contact-icon" viewBox="0 0 76 62" aria-hidden="true">
        <ellipse cx="38" cy="31" rx="37" ry="30" fill="var(--badge-yellow)"/>
        <path d="M38,58 C30,44 24,36 24,26 A14,14 0 0 1 52,26 C52,36 46,44 38,58 Z" fill="var(--shadow-black)"/>
        <circle cx="38" cy="25" r="5.5" fill="var(--badge-yellow)"/>
      </svg>
      <span class="contact-text">P.o.box 7316<br>Elmhaven, WY 80571</span>
    </li>
    <li class="contact-item contact-item--phone">
      <svg class="contact-icon" viewBox="0 0 76 62" aria-hidden="true">
        <ellipse cx="38" cy="31" rx="37" ry="30" fill="var(--badge-yellow)"/>
        <rect x="20" y="12" width="36" height="38" rx="6" fill="var(--shadow-black)"/>
        <path d="M31,18 C27,20 27,26 30,33 C33,40 38,45 43,45 C46,45 48,43 48,41 L43,37 C41,38 40,39 39,38 C36,35 34,31 34,28 C34,27 35,26 37,25 L35,18 Z" fill="var(--badge-yellow)"/>
      </svg>
      <span class="contact-text">970-555-0148</span>
    </li>
  </ul>
</div>
</body>
</html>
```